SilverLedgerOak - Double Sided Business Card

We are looking for design options or our business cards. We are a Business Solutions and HR solutions Provider - the theme is business, for this card.

Our brand colours are represented within our logo.

Details needed to be put on the front of the business card are:

Employees name: [Sample Name]
Role: [Sample Role]

Address: Suite 4 - Level 3/48 Halloran Avenue Parramatta NSW 2150
M: 0000 000 000
P: 1300 847 213
F: 1300 847 286
E: sample@silverledgeroak.com.au
www.silverledgeroak.com.au
Updates

Reason: Hello, could we please increase our deadline by 5 days. Thanking you, Tess

Target Market(s)

Business Owners, also Candidates looking for Employment

Industry/Entity Type

Business

Contact Information for Business Card

Role: [Sample Role]

M: 0000 000 000
P: 1300 847 213
F: 1300 847 286

Font styles to use
Sans Serif

Colors
3276b5
3176b5
0455a3
85abd2
cfdeed
ffffff
000000
1b1b1b
757575

Requirements
Must have
• Details needed to be put on the front of the business card are:
• Employees name: [Sample Name]
• Role: [Sample Role]
• Address: Suite 4 - Level 3/48 Halloran Avenue Parramatta NSW 2150
• M: 0000 000 000
• P: 1300 847 213
• F: 1300 847 286
• E: sample@silverledgeroak.com.au
• www.silverledgeroak.com.au
Nice to have
• Simplicity, clean and professional.

```html
<!DOCTYPE html>
<html lang="en">
<head>
<meta charset="utf-8">
<title>SilverLedgerOak – Business Card</title>
<link rel="stylesheet" href="https://fonts.googleapis.com/css2?family=Questrial&family=Arimo:wght@700&display=swap">
<style>
  :root {
    --brand-blue: #3276b5;
    --brand-deep: #0455a3;
    --brand-mid: #85abd2;
    --brand-pale: #cfdeed;
    --paper: #ffffff;
    --ink: #1b1b1b;
    --grey: #757575;
    --backdrop: #e9e9e9;
  }
  * { margin: 0; padding: 0; box-sizing: border-box; }
  html, body { width: 1200px; height: 1054px; overflow: hidden; }
  body {
    background: var(--backdrop);
    font-family: "Questrial", sans-serif;
    position: relative;
  }
  .card {
    position: absolute;
    left: 300px;
    width: 600px;
    height: 366px;
    background: var(--paper);
    box-shadow: 0 6px 18px rgba(0,0,0,0.12);
    overflow: hidden;
  }
  .card--front { top: 110px; }
  .card--back { top: 578px; }
  .card svg.shapes { position: absolute; inset: 0; }

  .brand-name {
    position: absolute;
    left: 0; right: 0;
    top: 178px;
    text-align: center;
    font-size: 46px;
    color: var(--brand-blue);
    letter-spacing: 0.5px;
  }
  .tagline {
    position: absolute;
    left: 0; right: 0;
    top: 262px;
    text-align: center;
    font-family: "Arimo", sans-serif;
    font-weight: 700;
    font-size: 15px;
    color: var(--ink);
  }

  .employee {
    position: absolute;
    left: 48px;
    top: 160px;
    color: var(--brand-blue);
    font-size: 17px;
    line-height: 1.3;
  }
  .employee .name, .employee .role-value {
    font-family: "Arimo", sans-serif;
    font-weight: 700;
  }
  .employee .name { display: block; padding-left: 14px; }
  .contact {
    position: absolute;
    left: 300px;
    top: 80px;
    width: 290px;
    text-align: center;
    color: var(--paper);
    font-size: 14.5px;
    line-height: 1.32;
  }
</style>
</head>
<body>

<section class="card card--front" aria-label="Card front">
  <svg class="shapes" width="600" height="366" viewBox="0 0 600 366">
    <polygon points="225,0 375,0 440,238 225,238" fill="var(--brand-mid)" opacity="0.8"/>
    <line x1="130" y1="250" x2="475" y2="250" stroke="var(--grey)" stroke-width="1.5"/>
  </svg>
  <div class="brand-name">SilverLedgerOak</div>
  <p class="tagline">Helping small to medium business realise their potential</p>
</section>

<section class="card card--back" aria-label="Card back">
  <svg class="shapes" width="600" height="366" viewBox="0 0 600 366">
    <g fill="none" stroke="var(--brand-mid)" stroke-width="1.5">
      <polygon points="150,225 350,225 350,330 150,330" transform="rotate(-8 250 278)"/>
      <polygon points="250,210 330,350 290,350 250,250"/>
      <polygon points="260,345 420,255 470,290 300,352"/>
    </g>
    <polygon points="270,78 575,38 592,300 300,268" fill="var(--brand-mid)" opacity="0.85"/>
  </svg>
  <div class="employee">
    Employees name:
    <span class="name">[SAMPLE NAME]</span>
    Role: <span class="role-value">[SAMPLE ROLE]</span>
  </div>
  <div class="contact">
    Mob: 0000 000 000<br>
    Tel: 1300 847 213<br>
    Fax: 1300 847 286<br>
    Suite 4 - Level 3/48<br>
    Halloran Avenue Parramatta<br>
    NSW 2150<br>
    Email: sample@silverledgeroak.com.au<br>
    www.silverledgeroak.com.au
  </div>
</section>

</body>
</html>
```